Maple Ridge business card design

Card needs to include the following text/items:
Company Logo
Tobin Marsh
Phone # - 555-318-7642
service@mapleridgelandscaping.example
Lawn & landscape maintenance services

```html
<!DOCTYPE html>
<html lang="en">
<head>
<meta charset="utf-8">
<title>Maple Ridge Landscaping – Business Card</title>
<link rel="stylesheet" href="https://fonts.googleapis.com/css2?family=Montserrat:wght@400;500;700&display=swap">
<style>
  :root {
    --forest: #0d4526;
    --ink: #333333;
    --paper: #ffffff;
    --backdrop: #e4e4e4;
    --on-band: #ffffff;
    --rule: rgba(255,255,255,0.6);
  }
  * { margin: 0; padding: 0; box-sizing: border-box; }
  html, body {
    width: 1200px; height: 900px; overflow: hidden;
    background: var(--backdrop);
    font-family: "Montserrat", Arial, sans-serif;
  }
  .sheet {
    position: relative; width: 1200px; height: 900px;
    display: flex; flex-direction: column; align-items: center;
    justify-content: center; gap: 40px;
  }
  .card {
    position: relative; width: 700px; height: 400px;
    background: var(--paper); border-radius: 18px; overflow: hidden;
    box-shadow: 0 6px 18px rgba(0,0,0,0.18);
  }
  .brand {
    display: flex; align-items: center; gap: 18px;
  }
  .brand-mark {
    border-radius: 50%;
    background: radial-gradient(circle at 40% 35%, #6ab04c, #2f6b2a 70%, #1f4d22);
  }
  .brand-name {
    color: var(--forest); font-weight: 700; letter-spacing: 0.5px;
    white-space: nowrap;
  }
  .card-front { display: flex; align-items: center; justify-content: center; }
  .card-front .brand-mark { width: 150px; height: 150px; }
  .card-front .brand-name { font-size: 44px; }

  .card-back .brand {
    position: absolute; top: 44px; left: 0; right: 0; justify-content: center;
  }
  .card-back .brand-mark { width: 118px; height: 118px; }
  .card-back .brand-name { font-size: 32px; }
  .band {
    position: absolute; left: 0; right: 0; top: 212px; height: 120px;
    background: var(--forest); color: var(--on-band);
    display: flex; align-items: center; justify-content: center; gap: 28px;
  }
  .person { text-align: right; }
  .person-name { font-size: 28px; font-weight: 700; }
  .person-title { font-size: 17px; font-weight: 400; margin-top: 2px; }
  .divider { width: 1px; height: 56px; background: var(--rule); }
  .contact { list-style: none; font-size: 17px; }
  .contact li { display: flex; align-items: center; gap: 12px; line-height: 1.7; }
  .contact svg { width: 18px; height: 18px; fill: var(--on-band); flex: none; }
  .tagline {
    position: absolute; left: 0; right: 0; top: 332px; height: 68px;
    display: flex; align-items: center; justify-content: center;
    font-size: 19px; color: var(--ink);
  }
</style>
</head>
<body>
<main class="sheet">
  <section class="card card-front" aria-label="Card front">
    <div class="brand">
      <div class="brand-mark" role="img" aria-label="Round landscape emblem with trees, fence and sun"></div>
      <span class="brand-name">Maple Ridge</span>
    </div>
  </section>

  <section class="card card-back" aria-label="Card back">
    <div class="brand">
      <div class="brand-mark" role="img" aria-label="Round landscape emblem with trees, fence and sun"></div>
      <span class="brand-name">Maple Ridge</span>
    </div>
    <div class="band">
      <div class="person">
        <div class="person-name">Tobin Marsh</div>
        <div class="person-title">CEO &amp; Founder</div>
      </div>
      <div class="divider"></div>
      <ul class="contact">
        <li>
          <svg viewBox="0 0 24 24" aria-hidden="true"><path d="M6.6 10.8a15.1 15.1 0 0 0 6.6 6.6l2.2-2.2a1 1 0 0 1 1-.25 11.4 11.4 0 0 0 3.6.57 1 1 0 0 1 1 1V20a1 1 0 0 1-1 1A17 17 0 0 1 3 4a1 1 0 0 1 1-1h3.5a1 1 0 0 1 1 1c0 1.25.2 2.45.57 3.57a1 1 0 0 1-.25 1z"/></svg>
          555-318-7642
        </li>
        <li>
          <svg viewBox="0 0 24 24" aria-hidden="true"><path d="M2 5h20v14H2z M2 5l10 7 10-7" fill="none" stroke="#fff" stroke-width="2"/></svg>
          service@mapleridgelandscaping.example
        </li>
      </ul>
    </div>
    <p class="tagline">Lawn &amp; landscape maintenance services</p>
  </section>
</main>
</body>
</html>
```